TrunvaX Calendar 2020 - Just need fine tuning

All design and content are ready. Just require some fine tuning
The date needs to be changed to 2020
and the address should be changed. I will provide new addresses.
Everything else can stay the same.

Other font styles liked:
• see file

Colors
a64599

```html
<!DOCTYPE html>
<html lang="en">
<head>
<meta charset="utf-8">
<title>TrunvaX Calendar 2020</title>
<link rel="stylesheet" href="https://fonts.googleapis.com/css2?family=Kaushan+Script&family=Arimo:wght@400;700&display=swap">
<style>
  :root {
    --brand: #a64599;
    --ink: #4a4a4a;
    --muted: #8a8a8a;
    --rule: #c9c9c9;
    --sunday: #e2335a;
    --paper: #ffffff;
    --jan: #e53f6f; --feb: #8d4aa8; --mar: #3f8fd4;
    --apr: #1fb3d6; --may: #22a58c; --jun: #1f9ab8;
    --jul: #4bb04a; --aug: #a5c63b; --sep: #f2a71b;
    --oct: #f28a1e; --nov: #e8443a; --dec: #d9262f;
  }
  * { margin: 0; padding: 0; box-sizing: border-box; }
  html, body { width: 730px; height: 1200px; overflow: hidden; background: var(--paper); }
  .calendar-card {
    position: relative; width: 730px; height: 1200px;
    font-family: "Arimo", Arial, sans-serif; color: var(--ink);
  }
  .masthead {
    position: absolute; top: 60px; left: 150px; right: 110px; height: 110px;
    display: flex; align-items: center; justify-content: space-between;
  }
  .brand { display: flex; align-items: center; gap: 12px; }
  .brand-dot { width: 20px; height: 20px; border-radius: 50%; background: var(--brand); }
  .brand-name {
    font-family: "Arimo", Arial, sans-serif; font-weight: 700; font-size: 38px;
    color: var(--brand); line-height: 1; letter-spacing: 0.5px;
  }
  .year {
    font-family: "Kaushan Script", cursive; font-size: 78px; color: var(--brand); line-height: 1;
  }
  .months {
    position: absolute; top: 200px; left: 48px; width: 640px;
    display: grid; grid-template-columns: repeat(3, 200px); column-gap: 20px;
    grid-auto-rows: 236px;
  }
  .month-name {
    font-family: "Kaushan Script", cursive; font-size: 34px; line-height: 44px;
    text-align: center; color: var(--accent); margin-bottom: 6px;
  }
  .weekdays, .days {
    display: grid; grid-template-columns: repeat(7, 1fr); text-align: center;
  }
  .weekdays {
    font-size: 15px; color: var(--muted); padding-bottom: 3px;
    border-bottom: 1.5px solid var(--rule); margin-bottom: 4px;
  }
  .days { font-size: 18px; line-height: 23px; color: var(--ink); }
  .days i { font-style: normal; }
  .days b { font-weight: 400; }
  .days > :nth-child(7n+1) { color: var(--sunday); }
  .jan { --accent: var(--jan); } .feb { --accent: var(--feb); } .mar { --accent: var(--mar); }
  .apr { --accent: var(--apr); } .may { --accent: var(--may); } .jun { --accent: var(--jun); }
  .jul { --accent: var(--jul); } .aug { --accent: var(--aug); } .sep { --accent: var(--sep); }
  .oct { --accent: var(--oct); } .nov { --accent: var(--nov); } .dec { --accent: var(--dec); }
</style>
</head>
<body>
<main class="calendar-card">
  <header class="masthead">
    <div class="brand"><span class="brand-dot"></span><span class="brand-name">TrunvaX</span></div>
    <div class="year">2020</div>
  </header>

  <section class="months">
    <article class="month jan"><h2 class="month-name">January</h2>
      <div class="weekdays"><span>S</span><span>M</span><span>T</span><span>W</span><span>T</span><span>F</span><span>S</span></div>
      <div class="days"><i></i><i></i><i></i><b>1</b><b>2</b><b>3</b><b>4</b><b>5</b><b>6</b><b>7</b><b>8</b><b>9</b><b>10</b><b>11</b><b>12</b><b>13</b><b>14</b><b>15</b><b>16</b><b>17</b><b>18</b><b>19</b><b>20</b><b>21</b><b>22</b><b>23</b><b>24</b><b>25</b><b>26</b><b>27</b><b>28</b><b>29</b><b>30</b><b>31</b></div>
    </article>
    <article class="month feb"><h2 class="month-name">February</h2>
      <div class="weekdays"><span>S</span><span>M</span><span>T</span><span>W</span><span>T</span><span>F</span><span>S</span></div>
      <div class="days"><i></i><i></i><i></i><i></i><i></i><i></i><b>1</b><b>2</b><b>3</b><b>4</b><b>5</b><b>6</b><b>7</b><b>8</b><b>9</b><b>10</b><b>11</b><b>12</b><b>13</b><b>14</b><b>15</b><b>16</b><b>17</b><b>18</b><b>19</b><b>20</b><b>21</b><b>22</b><b>23</b><b>24</b><b>25</b><b>26</b><b>27</b><b>28</b><b>29</b></div>
    </article>
    <article class="month mar"><h2 class="month-name">March</h2>
      <div class="weekdays"><span>S</span><span>M</span><span>T</span><span>W</span><span>T</span><span>F</span><span>S</span></div>
      <div class="days"><b>1</b><b>2</b><b>3</b><b>4</b><b>5</b><b>6</b><b>7</b><b>8</b><b>9</b><b>10</b><b>11</b><b>12</b><b>13</b><b>14</b><b>15</b><b>16</b><b>17</b><b>18</b><b>19</b><b>20</b><b>21</b><b>22</b><b>23</b><b>24</b><b>25</b><b>26</b><b>27</b><b>28</b><b>29</b><b>30</b><b>31</b></div>
    </article>

    <article class="month apr"><h2 class="month-name">April</h2>
      <div class="weekdays"><span>S</span><span>M</span><span>T</span><span>W</span><span>T</span><span>F</span><span>S</span></div>
      <div class="days"><i></i><i></i><i></i><b>1</b><b>2</b><b>3</b><b>4</b><b>5</b><b>6</b><b>7</b><b>8</b><b>9</b><b>10</b><b>11</b><b>12</b><b>13</b><b>14</b><b>15</b><b>16</b><b>17</b><b>18</b><b>19</b><b>20</b><b>21</b><b>22</b><b>23</b><b>24</b><b>25</b><b>26</b><b>27</b><b>28</b><b>29</b><b>30</b></div>
    </article>
    <article class="month may"><h2 class="month-name">May</h2>
      <div class="weekdays"><span>S</span><span>M</span><span>T</span><span>W</span><span>T</span><span>F</span><span>S</span></div>
      <div class="days"><i></i><i></i><i></i><i></i><i></i><b>1</b><b>2</b><b>3</b><b>4</b><b>5</b><b>6</b><b>7</b><b>8</b><b>9</b><b>10</b><b>11</b><b>12</b><b>13</b><b>14</b><b>15</b><b>16</b><b>17</b><b>18</b><b>19</b><b>20</b><b>21</b><b>22</b><b>23</b><b>24</b><b>25</b><b>26</b><b>27</b><b>28</b><b>29</b><b>30</b><b>31</b></div>
    </article>
    <article class="month jun"><h2 class="month-name">June</h2>
      <div class="weekdays"><span>S</span><span>M</span><span>T</span><span>W</span><span>T</span><span>F</span><span>S</span></div>
      <div class="days"><i></i><b>1</b><b>2</b><b>3</b><b>4</b><b>5</b><b>6</b><b>7</b><b>8</b><b>9</b><b>10</b><b>11</b><b>12</b><b>13</b><b>14</b><b>15</b><b>16</b><b>17</b><b>18</b><b>19</b><b>20</b><b>21</b><b>22</b><b>23</b><b>24</b><b>25</b><b>26</b><b>27</b><b>28</b><b>29</b><b>30</b></div>
    </article>

    <article class="month jul"><h2 class="month-name">July</h2>
      <div class="weekdays"><span>S</span><span>M</span><span>T</span><span>W</span><span>T</span><span>F</span><span>S</span></div>
      <div class="days"><i></i><i></i><i></i><b>1</b><b>2</b><b>3</b><b>4</b><b>5</b><b>6</b><b>7</b><b>8</b><b>9</b><b>10</b><b>11</b><b>12</b><b>13</b><b>14</b><b>15</b><b>16</b><b>17</b><b>18</b><b>19</b><b>20</b><b>21</b><b>22</b><b>23</b><b>24</b><b>25</b><b>26</b><b>27</b><b>28</b><b>29</b><b>30</b><b>31</b></div>
    </article>
    <article class="month aug"><h2 class="month-name">August</h2>
      <div class="weekdays"><span>S</span><span>M</span><span>T</span><span>W</span><span>T</span><span>F</span><span>S</span></div>
      <div class="days"><i></i><i></i><i></i><i></i><i></i><i></i><b>1</b><b>2</b><b>3</b><b>4</b><b>5</b><b>6</b><b>7</b><b>8</b><b>9</b><b>10</b><b>11</b><b>12</b><b>13</b><b>14</b><b>15</b><b>16</b><b>17</b><b>18</b><b>19</b><b>20</b><b>21</b><b>22</b><b>23</b><b>24</b><b>25</b><b>26</b><b>27</b><b>28</b><b>29</b><b>30</b><b>31</b></div>
    </article>
    <article class="month sep"><h2 class="month-name">September</h2>
      <div class="weekdays"><span>S</span><span>M</span><span>T</span><span>W</span><span>T</span><span>F</span><span>S</span></div>
      <div class="days"><i></i><i></i><b>1</b><b>2</b><b>3</b><b>4</b><b>5</b><b>6</b><b>7</b><b>8</b><b>9</b><b>10</b><b>11</b><b>12</b><b>13</b><b>14</b><b>15</b><b>16</b><b>17</b><b>18</b><b>19</b><b>20</b><b>21</b><b>22</b><b>23</b><b>24</b><b>25</b><b>26</b><b>27</b><b>28</b><b>29</b><b>30</b></div>
    </article>

    <article class="month oct"><h2 class="month-name">October</h2>
      <div class="weekdays"><span>S</span><span>M</span><span>T</span><span>W</span><span>T</span><span>F</span><span>S</span></div>
      <div class="days"><i></i><i></i><i></i><i></i><b>1</b><b>2</b><b>3</b><b>4</b><b>5</b><b>6</b><b>7</b><b>8</b><b>9</b><b>10</b><b>11</b><b>12</b><b>13</b><b>14</b><b>15</b><b>16</b><b>17</b><b>18</b><b>19</b><b>20</b><b>21</b><b>22</b><b>23</b><b>24</b><b>25</b><b>26</b><b>27</b><b>28</b><b>29</b><b>30</b><b>31</b></div>
    </article>
    <article class="month nov"><h2 class="month-name">November</h2>
      <div class="weekdays"><span>S</span><span>M</span><span>T</span><span>W</span><span>T</span><span>F</span><span>S</span></div>
      <div class="days"><b>1</b><b>2</b><b>3</b><b>4</b><b>5</b><b>6</b><b>7</b><b>8</b><b>9</b><b>10</b><b>11</b><b>12</b><b>13</b><b>14</b><b>15</b><b>16</b><b>17</b><b>18</b><b>19</b><b>20</b><b>21</b><b>22</b><b>23</b><b>24</b><b>25</b><b>26</b><b>27</b><b>28</b><b>29</b><b>30</b></div>
    </article>
    <article class="month dec"><h2 class="month-name">December</h2>
      <div class="weekdays"><span>S</span><span>M</span><span>T</span><span>W</span><span>T</span><span>F</span><span>S</span></div>
      <div class="days"><i></i><i></i><b>1</b><b>2</b><b>3</b><b>4</b><b>5</b><b>6</b><b>7</b><b>8</b><b>9</b><b>10</b><b>11</b><b>12</b><b>13</b><b>14</b><b>15</b><b>16</b><b>17</b><b>18</b><b>19</b><b>20</b><b>21</b><b>22</b><b>23</b><b>24</b><b>25</b><b>26</b><b>27</b><b>28</b><b>29</b><b>30</b><b>31</b></div>
    </article>
  </section>
</main>
</body>
</html>
```